Rebrand our dated accomodation business website "Tidewell Quay Residences"

we have a wordpress website ( www.tidewellquay.com.au) that is old and out dated .
I will need a new updated SQUARESPACE website (in which i already have ) with a fresh new design , also new logo and an easy site to manage from my end.
Need to connect our socials - facebook and instagram and our new site
Check out "brindle cove moorings" for inspiration...
These apartments are consists of -
-One bedroom One bath
-Two bedroom One bath
-Two bedroom Two bath
-Three bedroom Two bath
all other information is on our current website
KEEP it simple and fresh
ALSO WE DONT HAVE HUGE BIG BOATS IN THE MARINA SO PLEASE DONT HAVE THAT IN THE LOGO

Target Market(s)

Anyone looking for accomodation !! we have 64 rooms !!

Industry/Entity Type

accomodation / short stays

Coding

Coded - Design and coding required

Number of Pages Required

5+ page

Requirements
Must have
• Fresh , modern and easy to use.....have a hoilday vibe , also use natural colours
Nice to have
• i like accomodation website like ....https://fernandloft.com.au/luxury-coastal-accommodation/ or https://theorvanhotel.com/
Should not have
• please do not use bright colours and scripted fonts

```html
<!DOCTYPE html>
<html lang="en">
<head>
<meta charset="utf-8">
<title>Tidewell Quay Residences</title>
<link href="https://fonts.googleapis.com/css2?family=Montserrat:ital,wght@0,500;0,600;0,700;1,400&family=Lato:wght@400;700&display=swap" rel="stylesheet">
<style>
:root{
  --slate:#4a5a62;
  --slate-dark:#3f4c53;
  --ink:#3a4347;
  --text:#454c50;
  --muted:#5d6468;
  --mist:#f0fbfd;
  --line:#c9cfd2;
  --white:#ffffff;
  --panel:#f3f3f3;
}
*{box-sizing:border-box;margin:0;padding:0}
html,body{width:1200px;height:3881px;overflow:hidden;background:var(--white)}
body{position:relative;font-family:"Lato",sans-serif;color:var(--text)}
.abs{position:absolute}
h1,h2,h3,.brand{font-family:"Montserrat",sans-serif}
.btn{position:absolute;display:flex;align-items:center;justify-content:center;background:var(--slate);color:var(--white);font-family:"Lato",sans-serif;font-weight:700;font-size:17px;border-radius:3px;text-decoration:none}

/* header */
.topbar{position:absolute;left:372px;top:0;width:828px;height:33px;background:var(--slate);clip-path:polygon(18px 0,100% 0,100% 100%,0 100%);color:var(--white);font-size:14px}
.topbar span{position:absolute;top:8px}
.topbar .dot{width:20px;height:20px;border-radius:50%;background:var(--white);top:6px}
.logo-box{position:absolute;left:70px;top:0;width:228px;height:105px;background:var(--panel);display:flex;flex-direction:column;align-items:center;justify-content:center}
.logo-box .brand{font-size:21px;font-weight:500;color:var(--ink);letter-spacing:1px}
.logo-box small{font-size:9px;letter-spacing:4px;color:var(--ink);margin-top:3px}
.nav{position:absolute;top:68px;left:308px;display:flex;gap:25px;font-size:14px;color:var(--ink)}

/* hero */
.hero{position:absolute;left:0;top:119px;width:1200px;height:567px;background:linear-gradient(180deg,#b9c9cf 0%,#d9d6cc 35%,#e9e3d8 55%,#a88c6a 100%)}
.hero h1{position:absolute;left:108px;top:56px;font-size:53px;line-height:64px;color:var(--ink);font-weight:700}
.hero h1 em{font-weight:400}

/* section headings */
.sec-title{position:absolute;font-size:45px;font-weight:600;color:var(--ink);line-height:56px}
.rule{position:absolute;height:4px;background:var(--slate)}
.copy{position:absolute;font-size:14.5px;line-height:25.6px;text-align:justify;color:var(--text)}
.photo{position:absolute}
.frame{position:absolute;border:2px solid var(--slate);border-radius:6px}

/* accommodation */
.mist{position:absolute;left:0;top:1320px;width:1200px;height:725px;background:var(--mist)}
.guest-icon{position:absolute;width:148px;height:148px;border-radius:50%;background:var(--white);border:2px solid #dfe5e7;display:flex;align-items:center;justify-content:center}
.guest-title{position:absolute;width:300px;text-align:center;font-size:22px;font-weight:700;color:#2f3538}
.guest-text{position:absolute;width:250px;text-align:center;font-size:14px;line-height:23px;color:var(--text)}
.card{position:absolute;top:1915px;width:312px;height:425px;background:var(--white);border:2px solid #dde2e4;border-radius:6px}
.card .img{position:absolute;left:13px;top:13px;width:284px;height:291px}
.card h3{position:absolute;top:320px;width:100%;text-align:center;font-size:21px;font-weight:500;color:#2f3538}
.arrow{position:absolute;width:32px;height:32px;border-radius:50%;display:flex;align-items:center;justify-content:center}
.arrow.light{background:#a6abad}
.arrow.dark{background:var(--slate-dark)}

/* testimonials */
.review{position:absolute;top:3105px;width:315px;height:304px;background:var(--white);border:2px solid #e3e6e8;border-radius:6px}
.avatar{position:absolute;left:10px;top:20px;width:66px;height:66px;border-radius:50%;background:linear-gradient(#d7d8da,#9a9ea1)}
.review .name{position:absolute;left:96px;top:26px;font-size:21px;color:#2f3538}
.review .tag{position:absolute;left:96px;top:58px;font-size:17px;color:var(--muted)}
.review p{position:absolute;left:22px;top:106px;width:270px;font-size:14.5px;line-height:26px;text-align:justify;color:var(--muted);height:156px;overflow:hidden}
.review .more{position:absolute;left:22px;top:270px;font-size:14.5px;color:var(--muted);text-decoration:underline}

/* footer */
.footer{position:absolute;left:0;top:3500px;width:1200px;height:381px;background:var(--slate);color:var(--white)}
.footer h4{position:absolute;font-family:"Lato",sans-serif;font-weight:400;font-size:18px}
.footer ul{position:absolute;list-style:none;font-size:14px}
.footer li{height:34px;display:flex;align-items:center}
.footer li::before{content:"";width:7px;height:7px;border-radius:50%;background:var(--white);margin-right:16px}
.f-contact{position:absolute;left:875px;font-size:15px;line-height:25px;padding-left:24px}
.f-contact svg{position:absolute;left:0;top:5px}
</style>
</head>
<body>

<!-- header -->
<div class="topbar">
  <span style="left:82px">
    <svg width="16" height="16" viewBox="0 0 24 24" style="vertical-align:-3px;margin-right:4px"><path fill="#fff" d="M6.6 10.8a15 15 0 0 0 6.6 6.6l2.2-2.2a1 1 0 0 1 1-.25 11 11 0 0 0 3.6.6 1 1 0 0 1 1 1V20a1 1 0 0 1-1 1A17 17 0 0 1 3 4a1 1 0 0 1 1-1h3.5a1 1 0 0 1 1 1 11 11 0 0 0 .6 3.6 1 1 0 0 1-.25 1z"/></svg>1800 555 019 &nbsp;|&nbsp; (02) 5550 1846</span>
  <span style="left:385px">
    <svg width="18" height="13" viewBox="0 0 18 13" style="vertical-align:-2px;margin-right:6px"><rect x="1" y="1" width="16" height="11" fill="none" stroke="#fff" stroke-width="1.5"/><path d="M1 1l8 6 8-6" fill="none" stroke="#fff" stroke-width="1.5"/></svg>sales@tidewellquay.com.au</span>
  <span class="dot" style="left:662px"></span>
  <span class="dot" style="left:690px"></span>
</div>
<div class="logo-box">
  <div class="brand">TIDEWELL QUAY</div>
  <small>RESIDENCES</small>
</div>
<nav class="nav">
  <span>Home</span><span>About Us</span><span>Accommodation</span><span>Our Location</span><span>News/Events</span><span>Contact Us</span>
</nav>
<a class="btn" style="left:910px;top:57px;width:184px;height:47px">Book direct &amp; save!</a>

<!-- hero -->
<section class="hero" role="img" aria-label="Sunlit balcony lounge with white sofas overlooking the beach and ocean">
  <h1><em>Contemporary Self Contained</em><br>Apartments Brindle Cove<br>Jetty Precinct</h1>
</section>

<!-- about -->
<div class="frame" style="left:71px;top:808px;width:450px;height:422px"></div>
<div class="photo" role="img" aria-label="Bright open-plan living room with stone wall and ocean view" style="left:111px;top:771px;width:447px;height:418px;background:linear-gradient(135deg,#8e8a84 0%,#d8d4cc 45%,#bfc7c9 70%,#6e625a 100%);border-radius:4px"></div>
<h2 class="sec-title" style="left:643px;top:758px">About Tidewell<br>Quay Residences</h2>
<div class="rule" style="left:643px;top:886px;width:212px"></div>
<p class="copy" style="left:643px;top:918px;width:444px">Tidewell Quay Residences is a modern accommodation complex situated in the heart of Brindle Cove's vibrant Jetty precinct. The complex comprises 64 fully self-contained, privately owned apartments spread across three stories. Guests can choose from spacious 1, 2, or 3-bedroom apartments, each featuring modern decor, full kitchens, air-conditioned living areas, and private balconies or patios. Amenities include free Wi-Fi, cable TV, secure undercover parking, and direct lift access to all apartments</p>
<a class="btn" style="left:643px;top:1142px;width:131px;height:47px">Read More</a>

<!-- accommodation -->
<div class="mist"></div>
<h2 class="sec-title" style="left:0;width:1200px;text-align:center;top:1387px">Accommodation</h2>
<div class="rule" style="left:514px;top:1455px;width:171px"></div>
<p class="abs" style="left:0;width:1200px;text-align:center;top:1487px;font-size:15.5px;color:#2f3538">Whether you're visiting for an event or enjoying a well-earned vacation, we have the perfect apartment waiting just for you.</p>

<svg class="abs" style="left:0;top:1560px" width="1200" height="130">
  <path d="M318 90 C 390 130, 480 120, 540 105" fill="none" stroke="#6d7a80" stroke-width="2" stroke-dasharray="7 5"/>
  <path d="M672 32 C 740 10, 830 15, 884 40" fill="none" stroke="#6d7a80" stroke-width="2" stroke-dasharray="7 5"/>
</svg>

<div class="guest-icon" style="left:171px;top:1544px">
  <svg width="64" height="70" viewBox="0 0 64 70" fill="var(--slate)"><circle cx="18" cy="8" r="7"/><rect x="9" y="17" width="18" height="26" rx="4"/><rect x="11" y="40" width="6" height="28"/><rect x="19" y="40" width="6" height="28"/><circle cx="46" cy="8" r="7"/><path d="M38 17h16l6 30H32z"/><rect x="39" y="45" width="5" height="23"/><rect x="48" y="45" width="5" height="23"/></svg>
</div>
<div class="guest-icon" style="left:525px;top:1544px">
  <svg width="66" height="64" viewBox="0 0 66 64" fill="var(--slate)"><circle cx="12" cy="8" r="6"/><rect x="5" y="16" width="14" height="24" rx="3"/><rect x="6" y="38" width="5" height="24"/><rect x="13" y="38" width="5" height="24"/><circle cx="54" cy="8" r="6"/><path d="M47 16h14l5 26H42z"/><rect x="48" y="40" width="4" height="22"/><rect x="56" y="40" width="4" height="22"/><circle cx="33" cy="26" r="5"/><rect x="27" y="33" width="12" height="16" rx="3"/><rect x="28" y="47" width="4" height="15"/><rect x="34" y="47" width="4" height="15"/></svg>
</div>
<div class="guest-icon" style="left:881px;top:1544px">
  <svg width="66" height="66" viewBox="0 0 66 66" fill="var(--slate)"><circle cx="33" cy="33" r="24" fill="none" stroke="var(--slate)" stroke-width="6" stroke-dasharray="8 6"/><circle cx="33" cy="22" r="6"/><circle cx="20" cy="30" r="5"/><circle cx="46" cy="30" r="5"/><path d="M14 48 l12-10 h14 l12 10 l-6 6 H20z"/></svg>
</div>

<div class="guest-title" style="left:95px;top:1722px">Singles and couples</div>
<div class="guest-title" style="left:447px;top:1722px">Families</div>
<div class="guest-title" style="left:803px;top:1722px">Corporate guests</div>
<p class="guest-text" style="left:120px;top:1760px">can savour cocktail hour from the comfort of their private balcony or patio.</p>
<p class="guest-text" style="left:472px;top:1760px">will love the freedom to relax in their own space and prepare meals in a fully equipped kitchen.</p>
<p class="guest-text" style="left:828px;top:1760px">will feel right at home with secure surroundings, undercover parking, and all the comforts of a spacious,</p>

<div class="arrow light" style="left:43px;top:2089px"><svg width="12" height="14" viewBox="0 0 12 14"><path d="M9 1L3 7l6 6" fill="none" stroke="#fff" stroke-width="2.4"/></svg></div>
<div class="arrow dark" style="left:1127px;top:2089px"><svg width="12" height="14" viewBox="0 0 12 14"><path d="M3 1l6 6-6 6" fill="none" stroke="#fff" stroke-width="2.4"/></svg></div>

<div class="card" style="left:110px">
  <div class="img" role="img" aria-label="Warm one-bedroom apartment with mustard cushions and framed art" style="background:linear-gradient(150deg,#d9a65a 0%,#e6cf9c 50%,#8c6a45 100%)"></div>
  <h3>1 Bedroom Apartment</h3>
  <a class="btn" style="left:91px;top:360px;width:130px;height:46px">Book Now</a>
</div>
<div class="card" style="left:444px">
  <div class="img" role="img" aria-label="Two-bedroom apartment living room with orange sofa and garden windows" style="background:linear-gradient(160deg,#7e9a6e 0%,#c7c2b2 40%,#d8652a 75%,#8f5a3a 100%)"></div>
  <h3>2 Bedroom Apartment</h3>
  <a class="btn" style="left:91px;top:360px;width:130px;height:46px">Book Now</a>
</div>
<div class="card" style="left:778px">
  <div class="img" role="img" aria-label="Three-bedroom residence exterior at dusk" style="background:linear-gradient(180deg,#6a6f86 0%,#c6a58f 35%,#3d4550 65%,#242a30 100%)"></div>
  <h3>3 Bedroom Apartment</h3>
  <a class="btn" style="left:91px;top:360px;width:130px;height:46px">Book Now</a>
</div>

<!-- about location -->
<h2 class="sec-title" style="left:111px;top:2456px">About Brindle Cove</h2>
<div class="rule" style="left:111px;top:2528px;width:171px"></div>
<p class="copy" style="left:111px;top:2567px;width:444px">Visitors to Brindle Cove have the chance to explore a truly spectacular destination—where stunning beaches meet lush rainforests and scenic hinterland. A true vacation paradise, "Brindle" offers something for everyone. Stay up to date with the latest attractions and events by checking our blog regularly. Brindle Cove is also home to a world-class International Sports Stadium, hosting a wide range of exciting events throughout the year</p>
<a class="btn" style="left:111px;top:2798px;width:131px;height:47px">Read More</a>
<div class="frame" style="left:681px;top:2488px;width:449px;height:418px"></div>
<div class="photo" role="img" aria-label="Neutral-toned living room with curved sofa and timber kitchen" style="left:643px;top:2450px;width:446px;height:418px;background:linear-gradient(180deg,#8b8780 0%,#c9c2b8 45%,#ddd6cb 70%,#9c958b 100%)"></div>

<!-- feedback -->
<h2 class="sec-title" style="left:0;width:1200px;text-align:center;top:2985px">Guest Feedback</h2>
<div class="rule" style="left:514px;top:3058px;width:171px"></div>

<div class="arrow light" style="left:43px;top:3241px"><svg width="12" height="14" viewBox="0 0 12 14"><path d="M9 1L3 7l6 6" fill="none" stroke="#fff" stroke-width="2.4"/></svg></div>
<div class="arrow dark" style="left:1127px;top:3241px"><svg width="12" height="14" viewBox="0 0 12 14"><path d="M3 1l6 6-6 6" fill="none" stroke="#fff" stroke-width="2.4"/></svg></div>

<div class="review" style="left:107px">
  <div class="avatar" role="img" aria-label="Guest profile photo"></div>
  <div class="name">David</div><div class="tag">EXCELLENT</div>
  <p>It's a very nice place to stay in Brindle. Eateries are at the doorstep and many to choose from. beach is a couple of &lt;minutes walk. Train line is right at back door but it's not that intrusive at night. Stayed 3 times before now and will stay</p>
  <span class="more">Read More</span>
</div>
<div class="review" style="left:441px">
  <div class="avatar" role="img" aria-label="Guest profile photo"></div>
  <div class="name">Elizabeth</div><div class="tag">WE WILL VISIT AGAIN</div>
  <p>We just wanted to say thankyou to all at Tidewell Quay for our lovely stay at the weekend. On arrival we found our key in the safe. Our room was just beautiful. Even with the rain, nothing spoilt the weekend. The view was lovely to wake</p>
  <span class="more">Read More</span>
</div>
<div class="review" style="left:775px">
  <div class="avatar" role="img" aria-label="Guest profile photo"></div>
  <div class="name">Emma</div><div class="tag">AMAZING</div>
  <p>We loved everything about the accommodation and location. Proximity to the beaches at Brindle Cove, as well as restaurants and shops. We came by train, so had no car to get around in. No &lt;problem... everything was in walking</p>
  <span class="more">Read More</span>
</div>

<!-- footer -->
<footer class="footer">
  <div class="brand abs" style="left:111px;top:145px;font-size:26px;font-weight:500;letter-spacing:1px">TIDEWELL QUAY</div>
  <div class="abs" style="left:111px;top:180px;font-size:10px;letter-spacing:5px;width:230px;text-align:center">RESIDENCES</div>
  <div class="abs" style="left:111px;top:218px;width:232px;height:62px;background:var(--white);border-radius:4px">
    <span class="abs" style="left:16px;top:18px;width:54px;height:26px;border-radius:3px;background:#cfd4d6"></span>
    <span class="abs" style="left:88px;top:18px;width:58px;height:26px;border-radius:3px;background:#cfd4d6"></span>
    <span class="abs" style="left:164px;top:18px;width:52px;height:26px;border-radius:3px;background:#cfd4d6"></span>
  </div>

  <h4 style="left:425px;top:83px">Quick Links</h4>
  <ul style="left:425px;top:113px">
    <li>Home</li><li>About Us</li><li>Accommodation</li><li>Our Location</li><li>News/Events</li><li>Contact Us</li>
  </ul>

  <h4 style="left:609px;top:83px">Find Us</h4>
  <div class="abs" role="img" aria-label="Street map of the Brindle Cove jetty area" style="left:610px;top:125px;width:193px;height:139px;border-radius:4px;background:linear-gradient(135deg,#eef1ec 0%,#dfe8de 55%,#c9dbe6 100%)"></div>

  <h4 style="left:875px;top:83px">Contact Us</h4>
  <div class="f-contact" style="top:112px">
    <svg width="16" height="16" viewBox="0 0 24 24"><path fill="#fff" d="M12 2a7 7 0 0 0-7 7c0 5 7 13 7 13s7-8 7-13a7 7 0 0 0-7-7zm0 9.5A2.5 2.5 0 1 1 12 6.5a2.5 2.5 0 0 1 0 5z"/></svg>
    14 Harbourside Lane<br>Brindle Cove 2450
  </div>
  <div class="f-contact" style="top:193px">
    <svg width="16" height="16" viewBox="0 0 24 24"><circle cx="12" cy="12" r="11" fill="#fff"/><rect x="6" y="8" width="12" height="8" fill="none" stroke="#4a5a62" stroke-width="1.6"/><path d="M6 8l6 5 6-5" fill="none" stroke="#4a5a62" stroke-width="1.6"/></svg>
    sales@tidewellquay.com.au
  </div>
  <div class="f-contact" style="top:238px">
    <svg width="16" height="16" viewBox="0 0 24 24"><circle cx="12" cy="12" r="11" fill="#fff"/><path fill="#4a5a62" d="M8.5 10.8a9 9 0 0 0 4.7 4.7l1.5-1.5a.7.7 0 0 1 .7-.2 6 6 0 0 0 2 .3.7.7 0 0 1 .6.7V17a.7.7 0 0 1-.7.7A11 11 0 0 1 6.3 6.7.7.7 0 0 1 7 6h2.2a.7.7 0 0 1 .7.7 6 6 0 0 0 .3 2 .7.7 0 0 1-.2.7z"/></svg>
    1800 555 019<br>(02) 5550 1846
  </div>

  <div class="abs" style="left:111px;top:336px;width:976px;height:1px;background:#6f7c83"></div>
  <span class="abs" style="left:111px;top:350px;width:21px;height:21px;border-radius:50%;background:var(--white)"></span>
  <span class="abs" style="left:144px;top:350px;width:21px;height:21px;border-radius:50%;background:var(--white)"></span>
  <div class="abs" style="left:314px;top:352px;font-size:14px">Terms &amp; Conditions | Privacy Policy | Site Admin</div>
  <div class="abs" style="right:114px;top:352px;font-size:14px">© Tidewell Quay Residences. All Rights Reserved.</div>
</footer>

</body>
</html>
```